Dunworthy Business Cards & Stationary
Rehabilitation Nurse Case Manager
Dunworthy Business Cards & Stationary - Medical
Creative Brief
Professional
Owen Dunworthy RN, CRRN, QRP
PO Box 812 Cedar Hollow, ST 00000
owen@dunworthyandpartners.example
www.dunworthyandpartners.example
Please feel free to be creative. Would like design to be professional, innovative, and contemporary.
Large Logo with tagline, "Rehabilitation Nurse Case Manager" Also add bulleted listing of services we offer. These services are --Case Management -- Bill Review -- On-Site Analysis -- Home Safety Inspections

```html
<!DOCTYPE html>
<html lang="en">
<head>
<meta charset="utf-8">
<title>Dunworthy &amp; Associates Stationery</title>
<link href="https://fonts.googleapis.com/css2?family=Open+Sans:wght@400;600;700&display=swap" rel="stylesheet">
<style>
  :root {
    --backdrop: #6a4127;
    --paper: #ffffff;
    --navy: #1d2868;
    --blue: #2c4a9c;
    --grey: #8c8c8c;
    --ink: #333333;
    --faint: #e8eaf0;
  }
  * { box-sizing: border-box; margin: 0; padding: 0; }
  html, body { width: 1200px; height: 571px; overflow: hidden; }
  body {
    background: var(--backdrop);
    font-family: "Open Sans", Arial, sans-serif;
    color: var(--ink);
    position: relative;
  }
  .sheet, .envelope, .card {
    position: absolute;
    background: var(--paper);
    box-shadow: 0 2px 6px rgba(0,0,0,.35);
    overflow: hidden;
  }

  /* Brand lockup */
  .brand { position: absolute; display: flex; align-items: center; gap: 4px; }
  .brand__mark { width: 14px; height: 14px; border-radius: 50%; background: var(--navy); flex: none; }
  .brand__name { font-weight: 700; color: var(--navy); font-size: 5.5px; letter-spacing: .3px; line-height: 1.25; text-transform: uppercase; white-space: nowrap; }

  /* Letter-size sheets */
  .sheet { top: 91px; width: 298px; height: 442px; }
  .sheet--letterhead { left: 31px; }
  .sheet--fax { left: 379px; }
  .sheet .brand { top: 20px; left: 22px; }

  .watermark {
    position: absolute; top: 150px; left: 0; width: 100%;
    text-align: center; font-weight: 700; font-size: 32px;
    color: var(--faint); letter-spacing: 1px; text-transform: uppercase;
  }

  .waves { position: absolute; left: 0; bottom: 0; width: 100%; }
  .sheet .waves { height: 100px; }

  .footer-info {
    position: absolute; right: 12px; bottom: 12px;
    font-size: 3.6px; color: #fff; text-align: right; line-height: 1.5;
  }

  .fax-title { position: absolute; top: 84px; left: 22px; font-size: 14px; font-weight: 400; color: var(--ink); line-height: 1; }
  .fax-fields {
    position: absolute; top: 116px; left: 22px; right: 22px;
    display: grid; grid-template-columns: 1fr 1fr; column-gap: 22px; row-gap: 7px;
  }
  .fax-field { display: flex; align-items: flex-end; gap: 4px; font-size: 4.5px; line-height: 1; }
  .fax-field span:last-child { flex: 1; border-bottom: .6px solid var(--grey); height: 5px; }
  .fax-options {
    position: absolute; top: 196px; left: 22px; right: 22px;
    display: flex; justify-content: space-between; font-size: 4px; list-style: none;
  }
  .fax-options li { display: flex; align-items: center; gap: 3px; }
  .fax-options li::before { content: ""; width: 6px; height: 6px; border: .6px solid var(--grey); }

  /* Envelopes */
  .envelope { left: 744px; width: 432px; }
  .envelope--back-blue { top: 24px; height: 90px; }
  .envelope--back-grey { top: 100px; height: 80px; }
  .envelope--front { top: 163px; height: 156px; }
  .flap { position: absolute; top: 0; left: 0; width: 100%; height: 70px; }
  .envelope--back-blue .brand { top: 10px; left: 50%; transform: translateX(-50%); }
  .envelope--back-blue .brand__name { color: #fff; }
  .envelope--back-blue .brand__mark { background: #fff; }
  .envelope--front .brand { top: 22px; left: 18px; }
  .return-address { position: absolute; top: 44px; left: 18px; font-size: 3.8px; line-height: 1.5; }
  .envelope .waves { height: 50px; }

  /* Business cards */
  .card { top: 400px; width: 120px; height: 56px; }
  .card--contact { left: 809px; }
  .card--services { left: 948px; }
  .card .waves { height: 20px; }
  .card .brand__mark { width: 8px; height: 8px; }
  .card .brand__name { font-size: 3.6px; }
  .card__details { position: absolute; top: 5px; right: 6px; font-size: 3.2px; line-height: 1.5; text-align: right; }
  .card__details strong { font-size: 4px; color: var(--navy); }
  .card--contact .brand { top: 22px; left: 6px; }
  .tagline { position: absolute; top: 5px; left: 6px; font-size: 3.8px; font-weight: 600; color: var(--navy); }
  .card--services .brand { top: 18px; left: 6px; }
  .services { position: absolute; top: 14px; right: 6px; font-size: 3.2px; line-height: 1.55; list-style: none; }
  .services li::before { content: "• "; color: var(--blue); }
</style>
</head>
<body>

<svg width="0" height="0" style="position:absolute">
  <defs>
    <linearGradient id="greyFill" x1="0" y1="0" x2="1" y2="0">
      <stop offset="0" stop-color="#d9d9d9"/>
      <stop offset="1" stop-color="#7d7d7d"/>
    </linearGradient>
    <linearGradient id="blueFill" x1="0" y1="0" x2="0" y2="1">
      <stop offset="0" stop-color="#3a5bb0"/>
      <stop offset="1" stop-color="#1d2868"/>
    </linearGradient>
    <symbol id="swoosh" viewBox="0 0 300 110" preserveAspectRatio="none">
      <path d="M0 70 C80 20 170 30 300 52 L300 110 L0 110 Z" fill="url(#greyFill)"/>
      <path d="M0 62 C80 8 170 16 300 40" fill="none" stroke="#1d2868" stroke-width="5"/>
      <path d="M0 52 C90 4 180 8 300 30" fill="none" stroke="#2c4a9c" stroke-width="1.4"/>
      <path d="M0 78 C90 34 180 40 300 62" fill="none" stroke="#ffffff" stroke-width="2"/>
    </symbol>
  </defs>
</svg>

<section class="sheet sheet--letterhead">
  <div class="brand"><span class="brand__mark"></span><span class="brand__name">Dunworthy<br>&amp; Associates</span></div>
  <div class="watermark">Dunworthy</div>
  <svg class="waves" aria-hidden="true"><use href="#swoosh"/></svg>
  <p class="footer-info">PO Box 812 Cedar Hollow, ST 00000<br>owen@dunworthyandpartners.example<br>www.dunworthyandpartners.example</p>
</section>

<section class="sheet sheet--fax">
  <div class="brand"><span class="brand__mark"></span><span class="brand__name">Dunworthy<br>&amp; Associates</span></div>
  <h1 class="fax-title">FAX</h1>
  <div class="fax-fields">
    <div class="fax-field"><span>To:</span><span></span></div>
    <div class="fax-field"><span>From:</span><span></span></div>
    <div class="fax-field"><span>Fax:</span><span></span></div>
    <div class="fax-field"><span>Pages:</span><span></span></div>
    <div class="fax-field"><span>Phone:</span><span></span></div>
    <div class="fax-field"><span>Date:</span><span></span></div>
    <div class="fax-field"><span>Re:</span><span></span></div>
    <div class="fax-field"><span>CC:</span><span></span></div>
  </div>
  <ul class="fax-options">
    <li>Urgent</li><li>For Review</li><li>Please Comment</li><li>Please Reply</li><li>Please Recycle</li>
  </ul>
  <svg class="waves" aria-hidden="true"><use href="#swoosh"/></svg>
  <p class="footer-info">PO Box 812 Cedar Hollow, ST 00000<br>owen@dunworthyandpartners.example<br>www.dunworthyandpartners.example</p>
</section>

<section class="envelope envelope--back-blue">
  <svg class="flap" viewBox="0 0 432 70" preserveAspectRatio="none" aria-hidden="true">
    <path d="M0 0 H432 V44 C320 76 112 76 0 44 Z" fill="url(#blueFill)"/>
  </svg>
  <div class="brand"><span class="brand__mark"></span><span class="brand__name">Dunworthy</span></div>
</section>

<section class="envelope envelope--back-grey">
  <svg class="flap" viewBox="0 0 432 70" preserveAspectRatio="none" aria-hidden="true">
    <path d="M0 0 H432 V40 C320 72 112 72 0 40 Z" fill="url(#greyFill)"/>
  </svg>
</section>

<section class="envelope envelope--front">
  <div class="brand"><span class="brand__mark"></span><span class="brand__name">Dunworthy<br>&amp; Associates</span></div>
  <p class="return-address">PO Box 812 Cedar Hollow, ST 00000</p>
  <svg class="waves" aria-hidden="true"><use href="#swoosh"/></svg>
</section>

<section class="card card--contact">
  <p class="card__details"><strong>Owen Dunworthy RN, CRRN, QRP</strong><br>Phone 000-555-0148<br>owen@dunworthyandpartners.example<br>www.dunworthyandpartners.example</p>
  <div class="brand"><span class="brand__mark"></span><span class="brand__name">Dunworthy<br>&amp; Associates</span></div>
  <svg class="waves" aria-hidden="true"><use href="#swoosh"/></svg>
</section>

<section class="card card--services">
  <p class="tagline">Rehabilitation Nurse Case Manager</p>
  <div class="brand"><span class="brand__mark"></span><span class="brand__name">Dunworthy</span></div>
  <ul class="services">
    <li>Case Management</li><li>Bill Review</li><li>On-Site Analysis</li><li>Home Safety Inspections</li>
  </ul>
  <svg class="waves" aria-hidden="true"><use href="#swoosh"/></svg>
</section>

</body>
</html>
```